New business card with our logo

we finalized our logo with the help of pixel harbor - now we need a business card using that logo. we are a metal service center providing raw steel and metal products for fabricating, contractors, artists, etc. we have the wording for the back of the card figured out (attached, no deviations from text please), just need help putting it all together.
Contact Information for Business Card
would like the look of steel somehow incorporated in the design ... would like the black part of the logo to be steel or silver color (the S & MORROW)
Font styles to use
Other font styles liked:
- calibri, arial, similar to those, modern looking
Colors
Designer to choose colors to be used in the design.
Requirements
Must have
- Back of card must haves are attached (no deviations from wording please).
- FRONT of card:
- logo
- address
- name
- office tel
- cell
- fax
- website
- address
Nice to have
- incorporate the look of steel or element of steel somehow
- names of the staff on front not in all caps, i.e. Tereza not TEREZA
- this industry is more industrial, not coffee or flower shop so design should be aligned with that
- design should be classic and tasteful

```html
<!DOCTYPE html>
<html lang="en">
<head>
<meta charset="utf-8">
<title>Morrow Steel – Business Card</title>
<link rel="stylesheet" href="https://fonts.googleapis.com/css2?family=Roboto:wght@400;500;700;900&display=swap">
<style>
  :root {
    --steel-blue: #1a6fbf;
    --steel-blue-dark: #135a9e;
    --charcoal: #2f2f33;
    --paper: #ffffff;
    --stage: #e9ebee;
    --ink: #222226;
  }
  * { box-sizing: border-box; margin: 0; padding: 0; }
  html, body { width: 1200px; height: 880px; overflow: hidden; }
  body {
    background: var(--stage);
    font-family: "Roboto", Arial, sans-serif;
    position: relative;
  }
  .card {
    position: absolute;
    width: 560px;
    height: 320px;
    border-radius: 26px;
    overflow: hidden;
    box-shadow: 0 10px 28px rgba(0,0,0,0.18);
  }

  /* Back of card */
  .card-back {
    left: 60px; top: 80px;
    background: var(--steel-blue);
    color: var(--paper);
  }
  .back-brand {
    position: absolute;
    left: 110px; top: 80px;
    display: flex; align-items: center; gap: 22px;
  }
  .brand-circle {
    width: 86px; height: 86px;
    border: 6px solid var(--paper);
    border-radius: 50%;
    flex: none;
  }
  .back-name {
    font-weight: 700;
    font-size: 50px;
    line-height: 0.95;
    letter-spacing: 1px;
  }
  .back-name span { display: block; padding-left: 44px; }
  .services {
    position: absolute;
    left: 0; right: 0; top: 214px;
    text-align: center;
    font-weight: 500;
    font-size: 15px;
    line-height: 1.45;
  }

  /* Front of card */
  .card-front {
    left: 580px; top: 480px;
    background: var(--paper);
  }
  .front-art { position: absolute; inset: 0; }
  .front-brand {
    position: absolute;
    left: 34px; top: 38px;
    color: var(--paper);
    font-weight: 700;
    font-size: 42px;
    line-height: 0.95;
    letter-spacing: 1px;
  }
  .front-brand span { display: block; padding-left: 34px; }
  .mark {
    position: absolute;
    right: 26px; top: 18px;
    display: flex; align-items: center; gap: 10px;
  }
  .mark-circle {
    width: 26px; height: 26px;
    border: 4px solid var(--charcoal);
    border-radius: 50%;
  }
  .mark-name {
    font-weight: 700;
    font-size: 24px;
    color: var(--charcoal);
    letter-spacing: 1px;
  }
  .person {
    position: absolute;
    left: 36px; top: 176px;
  }
  .person-name {
    font-weight: 700;
    font-size: 20px;
    letter-spacing: 0.5px;
  }
  .first { color: var(--steel-blue); }
  .last { color: var(--ink); }
  .role { font-size: 14px; color: var(--ink); margin-top: -2px; }
  .contacts {
    position: absolute;
    left: 36px; top: 224px;
    list-style: none;
    font-size: 13.5px;
    color: var(--ink);
    line-height: 17px;
  }
  .contacts li { display: flex; align-items: center; gap: 8px; }
  .contacts svg { width: 13px; height: 13px; flex: none; }
  .address {
    position: absolute;
    right: 30px; top: 196px;
    text-align: right;
    font-size: 14px;
    color: var(--ink);
    line-height: 1.3;
  }
</style>
</head>
<body>

<section class="card card-back" aria-label="Back of business card">
  <div class="back-brand">
    <div class="brand-circle"></div>
    <h1 class="back-name">MORROW<span>STEEL</span></h1>
  </div>
  <p class="services">
    Structural Steel - Stainless &amp; Aluminum<br>
    Building Components - Rebar - Decking.... and more
  </p>
</section>

<section class="card card-front" aria-label="Front of business card">
  <svg class="front-art" viewBox="0 0 560 320" preserveAspectRatio="none" aria-hidden="true">
    <polygon points="0,0 470,0 440,150 0,150" fill="var(--steel-blue)"/>
    <polygon points="0,150 440,150 436,160 0,160" fill="var(--charcoal)"/>
  </svg>

  <h2 class="front-brand">MORROW<span>STEEL</span></h2>

  <div class="mark">
    <div class="mark-circle"></div>
    <span class="mark-name">MORROW</span>
  </div>

  <div class="person">
    <p class="person-name"><span class="first">DANIEL</span> <span class="last">REYES</span></p>
    <p class="role">Director</p>
  </div>

  <ul class="contacts">
    <li><svg viewBox="0 0 14 14"><circle cx="7" cy="7" r="6.3" fill="none" stroke="var(--steel-blue)" stroke-width="1.2"/><path d="M4.5 4.2h1.6l.6 1.6-.9.6a4.5 4.5 0 0 0 1.9 1.9l.6-.9 1.6.6v1.6c-3 .3-5.6-2.3-5.4-5.4z" fill="var(--steel-blue)"/></svg>555-210-4470</li>
    <li><svg viewBox="0 0 14 14"><circle cx="7" cy="7" r="6.3" fill="none" stroke="var(--steel-blue)" stroke-width="1.2"/><rect x="5" y="3.5" width="4" height="7" rx="0.8" fill="none" stroke="var(--steel-blue)" stroke-width="1"/></svg>555-210-4471</li>
    <li><svg viewBox="0 0 14 14"><circle cx="7" cy="7" r="6.3" fill="none" stroke="var(--steel-blue)" stroke-width="1.2"/><rect x="4" y="5.5" width="6" height="4" fill="var(--steel-blue)"/><rect x="5" y="3.8" width="4" height="1.4" fill="var(--steel-blue)"/></svg>555-210-4472</li>
    <li><svg viewBox="0 0 14 14"><circle cx="7" cy="7" r="6.3" fill="none" stroke="var(--steel-blue)" stroke-width="1.2"/><rect x="3.8" y="4.6" width="6.4" height="4.8" fill="none" stroke="var(--steel-blue)" stroke-width="1"/><path d="M3.8 4.6 7 7.3l3.2-2.7" fill="none" stroke="var(--steel-blue)" stroke-width="1"/></svg>info@morrowsteel.com</li>
    <li><svg viewBox="0 0 14 14"><circle cx="7" cy="7" r="6.3" fill="none" stroke="var(--steel-blue)" stroke-width="1.2"/><circle cx="7" cy="7" r="3.4" fill="none" stroke="var(--steel-blue)" stroke-width="1"/><path d="M3.6 7h6.8M7 3.6v6.8" stroke="var(--steel-blue)" stroke-width="0.9"/></svg>www.morrowsteel.net</li>
  </ul>

  <p class="address">P.O. Box 4821<br>Harbor Road, Ashford, USA</p>
</section>

</body>
</html>
```